Brilliant Design Needed For Stand Up Pouch - Drink Mix

We need a layout for our resealable stand-up pouch that holds our powered sports drink mix. Target audience is endurance athletes that enjoy marathon running, cycling, mountain biking, hiking and triathlon. Secondary audience are participants in team sports such soccer, lacrosse, football and basketball. Please review the attached project brief for full details. Thanks!

Target Market(s)

50/50 male/female, ages 20-50, USA, succesful, driven, educated. Active, healthy, athletic, outdoor lifestyle.

Industry/Entity Type

Fitness

Font styles to use
Sans Serif

Colors
33a6d7
3277b5
abd037

Requirements
Must have
• Please review the attached project brief for full details.
Nice to have
Should not have

```html
<!DOCTYPE html>
<html lang="en">
<head>
<meta charset="utf-8">
<title>Pacewell Hydration – Pouch Range</title>
<link rel="stylesheet" href="https://fonts.googleapis.com/css2?family=Montserrat:ital,wght@0,700;0,800;1,600;1,800&family=Source+Sans+3:ital,wght@0,300;0,400;0,600;0,700;1,300;1,400;1,600;1,700&display=swap">
<style>
  :root {
    --stage: #0b0b0d;
    --navy: #1c3f7a;
    --brand-cyan: #33a6d7;
    --brand-blue: #3277b5;
    --ink: #1d2340;
    --white: #ffffff;
    --seam: rgba(255,255,255,0.55);
    --sport-top: #e2fa86;
    --sport-mid: #8fdc4e;
    --sport-low: #2fae72;
    --sport-band: #24597a;
    --endur-top: #ece6fb;
    --endur-mid: #a186ea;
    --endur-low: #5b34d4;
    --endur-band: #4020c4;
    --ultra-top: #feeab0;
    --ultra-mid: #f79a62;
    --ultra-low: #e63a6c;
    --ultra-band: #df2469;
  }
  * { box-sizing: border-box; margin: 0; padding: 0; }
  html, body { width: 1200px; height: 1113px; overflow: hidden; }
  body {
    background: var(--stage);
    font-family: "Source Sans 3", sans-serif;
    color: var(--ink);
    position: relative;
  }

  .pouch {
    position: absolute;
    width: 300px;
    overflow: hidden;
    border-radius: 6px 6px 10px 10px;
    background: linear-gradient(160deg, var(--top) 0%, var(--mid) 50%, var(--low) 100%);
  }
  .pouch--sport { --top: var(--sport-top); --mid: var(--sport-mid); --low: var(--sport-low); --band: var(--sport-band); }
  .pouch--endurance { --top: var(--endur-top); --mid: var(--endur-mid); --low: var(--endur-low); --band: var(--endur-band); }
  .pouch--ultra { --top: var(--ultra-top); --mid: var(--ultra-mid); --low: var(--ultra-low); --band: var(--ultra-band); }

  .pouch--back { top: 48px; height: 440px; }
  .pouch--front { top: 560px; height: 500px; }
  .col-1 { left: 95px; }
  .col-2 { left: 450px; }
  .col-3 { left: 805px; }

  .zip {
    position: absolute; left: 0; right: 0; top: 14px; height: 8px;
    background: repeating-linear-gradient(90deg, var(--seam) 0 2px, transparent 2px 5px);
  }
  .label-panel {
    position: absolute; left: 95px; width: 110px; top: 0; height: 96px;
    background: var(--white);
    display: flex; align-items: flex-end; justify-content: center;
    padding-bottom: 18px;
  }
  .wordmark {
    display: flex; align-items: center; gap: 4px;
    font-family: "Montserrat", sans-serif; font-weight: 800;
    font-size: 15px; color: var(--navy); letter-spacing: 0.02em;
  }
  .wordmark-dot { width: 9px; height: 9px; border-radius: 50%; background: var(--brand-cyan); }

  .tagline {
    position: absolute; left: 0; right: 0;
    text-align: center; font-style: italic; font-weight: 600;
    font-size: 9px; color: var(--navy); letter-spacing: 0.02em;
  }

  /* Back panel */
  .pouch--back .tagline { top: 102px; }
  .mix-table {
    position: absolute; left: 24px; top: 124px; width: 142px;
    border-collapse: collapse; background: var(--white);
    font-size: 6.5px; font-weight: 600;
  }
  .mix-table th, .mix-table td { padding: 2px 4px; text-align: left; border-bottom: 1px solid var(--mid); }
  .mix-table th { font-weight: 700; }
  .nutrition-box {
    position: absolute; right: 22px; top: 118px; width: 112px; height: 58px;
    background: var(--white);
    font-size: 6px; font-weight: 700; text-align: center; padding-top: 4px;
  }
  .back-copy {
    position: absolute; left: 18px; right: 18px; top: 190px;
    text-align: center; font-size: 7px; line-height: 1.3;
  }
  .back-copy .directions { font-size: 7.5px; font-weight: 600; margin-bottom: 10px; }
  .back-copy .directions em { font-weight: 700; }
  .back-copy .distributor { font-size: 6.5px; margin-bottom: 10px; }
  .back-copy .formula-title { font-weight: 700; font-size: 7px; }
  .back-copy ul { list-style: none; margin: 2px 0 8px; font-size: 7px; }
  .back-copy ul li::before { content: "• "; }
  .back-copy .formula-note { font-size: 6.3px; }

  .base-band {
    position: absolute; left: 0; right: 0; bottom: 0;
    background: var(--band);
    border-radius: 50% 50% 0 0 / 26px 26px 0 0;
  }
  .pouch--back .base-band { height: 78px; }
  .badge-row {
    position: absolute; left: 0; right: 0; top: 26px;
    display: flex; justify-content: center; gap: 12px;
  }
  .badge { width: 24px; height: 24px; border-radius: 50%; border: 2px solid var(--white); }
  .badge--dark { background: #1a1a1a; }
  .badge--lime { background: #abd037; }
  .badge--green { background: #2fb34a; }

  /* Front panel */
  .pouch--front .label-panel { height: 106px; }
  .pouch--front .tagline { top: 112px; font-size: 10px; }
  .product-title {
    position: absolute; left: 0; right: 0; top: 124px;
    text-align: center; font-family: "Montserrat", sans-serif; font-weight: 800;
    font-size: 38px; letter-spacing: 0.08em; color: var(--navy);
  }
  .formula-name {
    position: absolute; left: 0; right: 0; top: 172px;
    text-align: center; font-style: italic; font-weight: 300;
    font-size: 21px; color: var(--navy);
  }
  .flavour {
    position: absolute; left: 0; right: 0; top: 202px;
    text-align: center; font-size: 9.5px; font-weight: 400; color: var(--white);
    letter-spacing: 0.02em;
  }
  .runner-art {
    position: absolute; left: 30px; top: 222px; width: 200px; height: 170px;
    border-radius: 40% 60% 30% 50%;
    background: radial-gradient(ellipse at 55% 45%, rgba(220,230,240,0.55), rgba(160,175,190,0.15) 70%, transparent 100%);
  }
  .duration-number {
    position: absolute; right: 32px; top: 300px;
    font-family: "Montserrat", sans-serif; font-style: italic; font-weight: 800;
    font-size: 92px; line-height: 1; color: var(--white);
  }
  .pouch--front .base-band {
    height: 112px;
    color: var(--white); text-align: center; padding-top: 24px;
  }
  .system-name { font-size: 12.5px; font-weight: 400; }
  .recommend { font-size: 12.5px; font-weight: 700; font-style: italic; }
  .servings { font-size: 11.5px; font-weight: 300; font-style: italic; margin-top: 2px; }
  .net-weight { font-size: 9px; font-weight: 600; margin-top: 3px; }
</style>
</head>
<body>

<!-- Back panels -->
<section class="pouch pouch--back pouch--sport col-1">
  <div class="zip"></div>
  <div class="label-panel"><span class="wordmark"><span class="wordmark-dot"></span>PACEWELL</span></div>
  <p class="tagline">HYDRATION BY DURATION</p>
  <table class="mix-table">
    <tr><th>To Make</th><th>Pacewell Mix</th><th>Cold Water</th></tr>
    <tr><td>12 FL OZ</td><td>1 Scoop</td><td>12 FL OZ</td></tr>
    <tr><td>24 FL OZ</td><td>2 Scoops</td><td>24 FL OZ</td></tr>
    <tr><td>1 Gallon</td><td>27 Scoops</td><td>1 Gallon</td></tr>
  </table>
  <div class="nutrition-box">NUTRITIONAL FACTS</div>
  <div class="back-copy">
    <p class="directions"><em>Directions:</em> Pour Pacewell drink mix powder into a bottle. Add water. Shake until powder completely dissolves.</p>
    <p class="distributor">Distributed by Pacewell Endurance Co., Lakeview, OR 97630<br>www.pacewell-mix.com</p>
    <p class="formula-title">Pacewell SPORT Formula:</p>
    <ul>
      <li>Zero calories</li>
      <li>Key Electrolytes</li>
      <li>Vitamin C</li>
      <li>Sweetened with All-Natural Stevia</li>
    </ul>
    <p class="formula-note">Pacewell Sport Formula is ideal for workouts lasting up to 1-hour. Efforts such as a 5K or 10K run, basketball or tennis. With zero calories, Pacewell Sport is also a great choice for everyday hydration.</p>
  </div>
  <div class="base-band">
    <div class="badge-row"><span class="badge badge--dark"></span><span class="badge badge--lime"></span><span class="badge badge--green"></span><span class="badge badge--dark"></span></div>
  </div>
</section>

<section class="pouch pouch--back pouch--endurance col-2">
  <div class="zip"></div>
  <div class="label-panel"><span class="wordmark"><span class="wordmark-dot"></span>PACEWELL</span></div>
  <p class="tagline">HYDRATION BY DURATION</p>
  <table class="mix-table">
    <tr><th>To Make</th><th>Pacewell Mix</th><th>Cold Water</th></tr>
    <tr><td>12 FL OZ</td><td>1 Scoop</td><td>12 FL OZ</td></tr>
    <tr><td>24 FL OZ</td><td>2 Scoops</td><td>24 FL OZ</td></tr>
    <tr><td>1 Gallon</td><td>27 Scoops</td><td>1 Gallon</td></tr>
  </table>
  <div class="nutrition-box">NUTRITIONAL FACTS</div>
  <div class="back-copy">
    <p class="directions"><em>Directions:</em> Pour Pacewell drink mix powder into a bottle. Add water. Shake until powder completely dissolves.</p>
    <p class="distributor">Distributed by Pacewell Endurance Co., Lakeview, OR 97630<br>www.pacewell-mix.com</p>
    <p class="formula-title">Pacewell ENDURANCE Formula:</p>
    <ul>
      <li>90 calories per serving</li>
      <li>carbohydrates for Sustaining Energy</li>
      <li>Complete Electrolytes</li>
      <li>Vitamin C</li>
    </ul>
    <p class="formula-note">Pacewell Endurance Formula is ideal for workouts lasting up to 2-hours. Efforts such as a half marathon, cycling, triathlon, soccer, lacrosse and football. With carbohydrates, electrolytes and vitamin C, Pacewell Endurance Formula is a great choice for athletes striving to be their best.</p>
  </div>
  <div class="base-band">
    <div class="badge-row"><span class="badge badge--dark"></span><span class="badge badge--lime"></span><span class="badge badge--green"></span><span class="badge badge--dark"></span></div>
  </div>
</section>

<section class="pouch pouch--back pouch--ultra col-3">
  <div class="zip"></div>
  <div class="label-panel"><span class="wordmark"><span class="wordmark-dot"></span>PACEWELL</span></div>
  <p class="tagline">HYDRATION BY DURATION</p>
  <table class="mix-table">
    <tr><th>To Make</th><th>Pacewell Mix</th><th>Cold Water</th></tr>
    <tr><td>12 FL OZ</td><td>1 Scoop</td><td>12 FL OZ</td></tr>
    <tr><td>24 FL OZ</td><td>2 Scoops</td><td>24 FL OZ</td></tr>
    <tr><td>1 Gallon</td><td>27 Scoops</td><td>1 Gallon</td></tr>
  </table>
  <div class="nutrition-box">NUTRITIONAL FACTS</div>
  <div class="back-copy">
    <p class="directions"><em>Directions:</em> Pour Pacewell drink mix powder into a bottle. Add water. Shake until powder completely dissolves.</p>
    <p class="distributor">Distributed by Pacewell Endurance Co., Lakeview, OR 97630<br>www.pacewell-mix.com</p>
    <p class="formula-title">Pacewell ULTRA Formula:</p>
    <ul>
      <li>250 calories per serving</li>
      <li>Carbohydrates for sustained energy</li>
      <li>Complete Electrolytes</li>
      <li>Vitamin C</li>
      <li>Caffeine</li>
    </ul>
    <p class="formula-note">Pacewell ULTRA Formula is designed for long-lasting workouts of 3-hours or more. This formula is designed to support marathons and ultra-marathons, ironman triathlons, cycling and mountain biking, and hiking. With increased levels of carbohydrates and electrolytes, along with Vitamin C and caffeine, Pacewell ULTRA Formula is a great choice for extreme athletes pushing their limits.</p>
  </div>
  <div class="base-band">
    <div class="badge-row"><span class="badge badge--dark"></span><span class="badge badge--lime"></span><span class="badge badge--green"></span><span class="badge badge--dark"></span></div>
  </div>
</section>

<!-- Front panels -->
<section class="pouch pouch--front pouch--sport col-1">
  <div class="zip"></div>
  <div class="label-panel"><span class="wordmark"><span class="wordmark-dot"></span>PACEWELL</span></div>
  <p class="tagline">HYDRATION BY DURATION</p>
  <h2 class="product-title">HYDRATION</h2>
  <p class="formula-name">Sport Formula Drink Mix</p>
  <p class="flavour">LEMON-LIME WITH OTHER NATURAL FLAVOURS</p>
  <div class="runner-art" role="img" aria-label="Runner figure dissolving into powder particles"></div>
  <span class="duration-number">1</span>
  <div class="base-band">
    <p class="system-name">Advanced Hydration System</p>
    <p class="recommend">Recommended for workouts lasting 1 hour</p>
    <p class="servings">Makes 27, 12 fl oz Servings</p>
    <p class="net-weight">NET WT. 15.5 OZ (440G)</p>
  </div>
</section>

<section class="pouch pouch--front pouch--endurance col-2">
  <div class="zip"></div>
  <div class="label-panel"><span class="wordmark"><span class="wordmark-dot"></span>PACEWELL</span></div>
  <p class="tagline">HYDRATION BY DURATION</p>
  <h2 class="product-title">HYDRATION</h2>
  <p class="formula-name">Endurance Formula Drink Mix</p>
  <p class="flavour">LEMON-LIME WITH OTHER NATURAL FLAVOURS</p>
  <div class="runner-art" role="img" aria-label="Runner figure dissolving into powder particles"></div>
  <span class="duration-number">2</span>
  <div class="base-band">
    <p class="system-name">Advanced Hydration System</p>
    <p class="recommend">Recommended for workouts lasting 2 hours</p>
    <p class="servings">Makes 27, 12 fl oz Servings</p>
    <p class="net-weight">NET WT. 15.5 OZ (440G)</p>
  </div>
</section>

<section class="pouch pouch--front pouch--ultra col-3">
  <div class="zip"></div>
  <div class="label-panel"><span class="wordmark"><span class="wordmark-dot"></span>PACEWELL</span></div>
  <p class="tagline">HYDRATION BY DURATION</p>
  <h2 class="product-title">HYDRATION</h2>
  <p class="formula-name">Ultra Formula Drink Mix</p>
  <p class="flavour">LEMON-LIME WITH OTHER NATURAL FLAVOURS</p>
  <div class="runner-art" role="img" aria-label="Runner figure dissolving into powder particles"></div>
  <span class="duration-number">3</span>
  <div class="base-band">
    <p class="system-name">Advanced Hydration System</p>
    <p class="recommend">Recommended for workouts lasting 3 hours</p>
    <p class="servings">Makes 27, 12 fl oz Servings</p>
    <p class="net-weight">NET WT. 15.5 OZ (440G)</p>
  </div>
</section>

</body>
</html>
```